Seminar Workbook Template

My first project is a Workbook Template. There is a sample attached to give you an idea of the layout I like. I have added notes, in blue, to show what I want. I do want a header that will brand the workbook (should have the logo). We are looking for someone that we can continue to work 1 -1 with other, collateral projects. We want a constant look and feel and we have two projects ready to go.

Target Market(s)

My clients are Office Managers and CPAs so I want the workbook to have a professional layout and match the look and feel of my website: LedgerVineworks.com

Requirements
Must have
• Must match the feel of the Website. Must be in Word .doc format.
Should not have
• No red.

```html
<!DOCTYPE html>
<html lang="en">
<head>
<meta charset="UTF-8">
<title>Workbook – Module 1 Lesson 3</title>
<link rel="stylesheet" href="https://fonts.googleapis.com/css2?family=Montserrat:wght@500;600;700;800&family=Open+Sans:wght@400;600&family=Crimson+Text:wght@400&display=swap">
<style>
  :root{
    --backdrop:#8e8e8e;
    --paper:#ffffff;
    --header-tint:#e4e4e4;
    --brand-green:#3db381;
    --title-green:#124a2c;
    --ink:#1b1b1b;
    --rule:#a9a9a9;
    --body:#222222;
    --on-green:#eaf7f0;
  }
  *{box-sizing:border-box;margin:0;padding:0}
  html,body{width:1200px;height:800px;overflow:hidden}
  body{background:var(--backdrop);font-family:"Open Sans",sans-serif;color:var(--body)}
  .spread{position:absolute;left:20px;top:20px;width:1160px;height:760px;display:flex;box-shadow:0 8px 24px rgba(0,0,0,.25)}
  .page{position:relative;width:580px;height:760px;background:var(--paper);overflow:hidden}
  .page--left{box-shadow:inset -14px 0 18px -14px rgba(0,0,0,.18)}
  .page--right{box-shadow:inset 14px 0 18px -14px rgba(0,0,0,.18)}

  .page-header{height:92px;background:linear-gradient(180deg,var(--header-tint),#fafafa);display:flex;align-items:center;justify-content:space-between;padding:0 28px}
  .brand{display:flex;align-items:center;gap:8px;font-family:"Montserrat",sans-serif;font-weight:700;font-size:11px;letter-spacing:.08em;color:var(--title-green);text-transform:uppercase}
  .brand-dot{width:14px;height:14px;border-radius:50%;background:var(--brand-green)}
  .lesson-title{text-align:right;font-family:"Montserrat",sans-serif;color:var(--title-green)}
  .lesson-title h1{font-size:21px;font-weight:800;letter-spacing:.01em}
  .lesson-title p{font-size:15px;font-weight:500;margin-top:2px}

  .page-body{position:absolute;top:108px;left:26px;right:26px;bottom:62px}
  .page-footer{position:absolute;left:0;right:0;bottom:0;height:48px;background:var(--brand-green);display:flex;align-items:center;justify-content:center;font-size:9.5px;color:#fff;font-family:"Open Sans",sans-serif}
  .page-number{position:absolute;font-size:9px;font-weight:600}
  .page--left .page-number{left:24px}
  .page--right .page-number{right:24px}

  .pill{background:var(--ink);color:#fff;border-radius:14px;height:34px;display:flex;align-items:center;justify-content:center;font-family:"Montserrat",sans-serif;font-weight:700;font-size:11px;letter-spacing:.04em;text-transform:uppercase}
  .write-line{height:24px;border-bottom:1px dotted var(--rule)}
  .check-row{display:flex;align-items:flex-end;gap:10px}
  .check-row .circle{width:13px;height:13px;border:1.3px solid #444;border-radius:50%;flex:none;margin-bottom:3px}
  .check-row .lines{flex:1}

  .green-panel{background:var(--brand-green);border-radius:10px;color:var(--on-green);font-family:"Crimson Text",serif;font-size:12px;line-height:1.3;padding:20px 16px}
  .green-panel p+p{margin-top:12px}

  /* left page */
  .left-grid{display:grid;grid-template-columns:212px 1fr;gap:22px;height:100%}
  .listening .pill{margin:16px 0 6px}
  .listening .write-line{height:22px}
  .listening .check-row{margin-bottom:8px}
  .todo-list{list-style:none;margin:16px 0 16px 4px;font-size:11px;line-height:1.25}
  .todo-list li{position:relative;padding-left:24px;margin-bottom:9px}
  .todo-list li::before{content:"";position:absolute;left:0;top:2px;width:11px;height:11px;border-radius:50%;background:var(--ink)}
  .etc-rows{margin:6px 0 18px}
  .stuck-lines{margin-top:8px}

  /* right page */
  .right-top{display:grid;grid-template-columns:1fr 262px;gap:24px;align-items:start}
  .wins-lines{margin:6px 0 22px}
  .duration-text{font-size:11.5px;line-height:1.38;margin-top:12px;padding-right:4px}
  .tip-panel{padding:20px 18px}
  .tip-panel h2{font-family:"Montserrat",sans-serif;font-weight:700;font-size:11.5px;letter-spacing:.03em;color:var(--on-green);margin-bottom:12px;line-height:1.3}
  .ideas{margin-top:16px}
  .ideas .write-line{height:26px}
</style>
</head>
<body>
<div class="spread">
  <section class="page page--left">
    <header class="page-header">
      <div class="brand"><span class="brand-dot"></span>Ledger Vineworks</div>
      <div class="lesson-title"><h1>MODULE 1 | LESSON 3</h1><p>Research Your Audience</p></div>
    </header>
    <div class="page-body left-grid">
      <div class="column">
        <div class="green-panel intro-panel">
          <p>Your successful eCourse is going to not only leverage your talents, it's going to address a pressing need, or problem, a goal or aspiration of your audience.</p>
          <p>Your students need to leave the course “transformed” whether that's newly capable of a skill, moved to a new way of living, earning more money, or even feeling healthier.</p>
          <p>Defining a “problem” you can help with is the beginning of using that “problem-promise-path” framework for your course design—and the route to that is through audience research.</p>
        </div>
        <div class="listening">
          <div class="pill">3 Listening Posts</div>
          <div class="check-row"><span class="circle"></span><div class="lines"><div class="write-line"></div><div class="write-line"></div></div></div>
          <div class="check-row"><span class="circle"></span><div class="lines"><div class="write-line"></div><div class="write-line"></div></div></div>
          <div class="check-row"><span class="circle"></span><div class="lines"><div class="write-line"></div><div class="write-line"></div></div></div>
        </div>
      </div>
      <div class="column">
        <div class="pill">To Be Done</div>
        <ul class="todo-list">
          <li>View lesson 1.3</li>
          <li>Identify communities for social listening</li>
          <li>Listen and track problems, goals, and obstacles (worksheet)</li>
          <li>Research via web search</li>
          <li>Research via existing books, videos and classes</li>
          <li>Research via survey</li>
        </ul>
        <div class="pill">Etc...</div>
        <div class="etc-rows">
          <div class="check-row"><span class="circle"></span><div class="lines"><div class="write-line"></div></div></div>
          <div class="check-row"><span class="circle"></span><div class="lines"><div class="write-line"></div></div></div>
          <div class="check-row"><span class="circle"></span><div class="lines"><div class="write-line"></div></div></div>
          <div class="check-row"><span class="circle"></span><div class="lines"><div class="write-line"></div></div></div>
        </div>
        <div class="pill">Stuck | Stalled | Need Help</div>
        <div class="stuck-lines">
          <div class="write-line"></div><div class="write-line"></div><div class="write-line"></div><div class="write-line"></div><div class="write-line"></div><div class="write-line"></div>
        </div>
      </div>
    </div>
    <footer class="page-footer"><span class="page-number">18</span>Copyright © 2019 Marta Quillen | ClassCraftStudio.com Course Roadmap. All rights reserved.</footer>
  </section>

  <section class="page page--right">
    <header class="page-header">
      <div class="brand"><span class="brand-dot"></span>Ledger Vineworks</div>
      <div class="lesson-title"><h1>MODULE 1 | LESSON 3</h1><p>Research Your Audience</p></div>
    </header>
    <div class="page-body">
      <div class="right-top">
        <div class="column">
          <div class="pill">Ah-Has &amp; Wins</div>
          <div class="wins-lines"><div class="write-line"></div><div class="write-line"></div><div class="write-line"></div><div class="write-line"></div></div>
          <div class="pill">How Long Should This Take?</div>
          <p class="duration-text">This one's going to take some work time AND some elapsed time. Expect to spend 2 to 4 hours researching and setting up your listening stations. And then you need to “listen.” Move onto the next lesson even as you keep listening and researching.</p>
        </div>
        <aside class="green-panel tip-panel">
          <h2>PRO COURSE<br>BUILDING TIP:</h2>
          <p>As you record what you hear from your audience . . . use the exact language they are using. Copy their comments and paste into your notes. You'll use this later in your marketing materials.</p>
          <p>As you record what you hear from your audience . . . use the exact language they are using. Copy their comments and paste into your notes. You'll use this later in your marketing materials.</p>
          <p>As you record what you hear from your audience.</p>
        </aside>
      </div>
      <div class="ideas">
        <div class="pill">Ideas &amp; Notes</div>
        <div class="write-line"></div><div class="write-line"></div><div class="write-line"></div><div class="write-line"></div><div class="write-line"></div><div class="write-line"></div><div class="write-line"></div>
      </div>
    </div>
    <footer class="page-footer"><span class="page-number">19</span>Copyright © 2019 Marta Quillen | ClassCraftStudio.com Course Roadmap. All rights reserved.</footer>
  </section>
</div>
</body>
</html>
```